Small Box Design - For launch into retail market

We need artwork for small boxes that we are going to be using for the retail market. I will upload the type of box we are going to be using. The example we are uploading is of a different company that sells the same products. We would like our Logo on the box as as our web address (www.brandellgroup-ltd.com). The rest is up to you. Please contact with any questions.

Target Market(s)

Distributors, Retailers of Fasteners

Industry/Entity Type

Manufacture

Colors
0355a3
3176b5
fbee3f
fbf289

Requirements
Must have
• Our logo, our web address www.brandellgroup-ltd.com
• Somewhere on the box Washers . Stampings . Assemblies . Bearings (most likely below our logo somewhere)
Nice to have
• Blue is our corporate colour, but it's not essential. You can suggest any colours and we will consider.

```html
<!DOCTYPE html>
<html lang="en">
<head>
<meta charset="utf-8">
<title>Brandell Group – Retail Carton Dieline</title>
<link href="https://fonts.googleapis.com/css2?family=Montserrat:wght@400;600;700&display=swap" rel="stylesheet">
<style>
  :root {
    --bg-stage: #a5a8aa;
    --carton-blue: #053a86;
    --carton-edge: #032f70;
    --fold-line: rgba(255,255,255,0.75);
    --ink-white: #ffffff;
    --accent-gold: #c9a15a;
    --band-white: #ffffff;
  }
  html, body {
    margin: 0;
    padding: 0;
    width: 972px;
    height: 1200px;
    overflow: hidden;
    background: var(--bg-stage);
  }
  .dieline {
    display: block;
    width: 972px;
    height: 1200px;
    font-family: "Montserrat", Arial, sans-serif;
  }
  .carton-body { fill: var(--carton-blue); stroke: var(--carton-edge); stroke-width: 6; }
  .fold { stroke: var(--fold-line); stroke-width: 1; fill: none; }
  .url-band { fill: var(--band-white); }
  .url-text { fill: var(--accent-gold); font-size: 14px; font-weight: 600; letter-spacing: 3.2px; }
  .brand-name { fill: var(--ink-white); font-size: 26px; font-weight: 600; }
  .brand-name-lid { font-size: 28px; }
  .brand-services { fill: var(--ink-white); font-size: 9px; font-weight: 400; letter-spacing: 0.4px; }
  .lid-url { fill: var(--accent-gold); font-size: 13px; font-weight: 600; letter-spacing: 3.5px; }
  .lid-heading { fill: var(--ink-white); font-size: 8.5px; font-weight: 600; }
  .lid-copy { fill: var(--ink-white); font-size: 8.5px; font-weight: 400; }
  .carton-label { fill: var(--ink-white); font-size: 6px; font-weight: 700; }
  .carton-number { fill: var(--ink-white); font-size: 24px; font-weight: 700; }
  .recycle-ring { fill: none; stroke: var(--ink-white); stroke-width: 9; }
  .recycle-head { fill: var(--ink-white); }
</style>
</head>
<body>
<svg class="dieline" viewBox="0 0 1215 1500" xmlns="http://www.w3.org/2000/svg">
  <path class="carton-body" role="img" aria-label="Blue carton surface with a soft washer-ring background pattern"
        d="M440,330 L305,330 Q285,330 285,305 L285,250 Q285,120 440,105 L835,105 Q1000,120 1000,250 L1000,305 Q1000,330 980,330 L835,330 L835,410 L930,410 L940,400 L1000,400 L1010,410 L1110,410 L1110,595 L1122,607 L1122,928 L835,928 L835,1095 L1122,1095 L1122,1320 L152,1320 L152,1095 L440,1095 L440,928 L152,928 L152,607 L165,595 L165,410 L265,410 L275,400 L335,400 L345,410 L440,410 Z"/>

  <g class="fold">
    <path d="M448,320 L300,320 Q292,320 292,305 L292,250 Q292,130 448,112"/>
    <path d="M826,320 L985,320 Q993,320 993,305 L993,250 Q993,130 826,112"/>
    <line x1="448" y1="112" x2="826" y2="112"/>
    <line x1="448" y1="112" x2="448" y2="1312"/>
    <line x1="826" y1="112" x2="826" y2="1312"/>
    <line x1="448" y1="320" x2="826" y2="320"/>
    <path d="M175,607 L175,420 L435,420 L435,595 L448,607"/>
    <path d="M1102,607 L1102,420 L840,420 L840,595 L826,607"/>
    <line x1="162" y1="607" x2="1112" y2="607"/>
    <line x1="162" y1="607" x2="162" y2="920"/>
    <line x1="1112" y1="607" x2="1112" y2="920"/>
    <line x1="162" y1="817" x2="1112" y2="817"/>
    <line x1="162" y1="920" x2="448" y2="920"/>
    <line x1="826" y1="920" x2="1112" y2="920"/>
    <rect x="162" y="1103" width="950" height="209"/>
  </g>

  <g class="brand-panel">
    <text class="brand-name" x="305" y="722" text-anchor="middle">Brandell Group</text>
    <text class="brand-services" x="305" y="744" text-anchor="middle">WASHERS . STAMPINGS . ASSEMBLIES . BEARINGS</text>

    <text class="brand-name" x="637" y="722" text-anchor="middle">Brandell Group</text>
    <text class="brand-services" x="637" y="744" text-anchor="middle">WASHERS . STAMPINGS . ASSEMBLIES . BEARINGS</text>

    <text class="brand-name" x="969" y="722" text-anchor="middle">Brandell Group</text>
    <text class="brand-services" x="969" y="744" text-anchor="middle">WASHERS . STAMPINGS . ASSEMBLIES . BEARINGS</text>
  </g>

  <rect class="url-band" x="152" y="767" width="970" height="20"/>
  <text class="url-text" x="305" y="782" text-anchor="middle">www.brandellgroup-ltd.com</text>
  <text class="url-text" x="637" y="782" text-anchor="middle">www.brandellgroup-ltd.com</text>
  <text class="url-text" x="969" y="782" text-anchor="middle">www.brandellgroup-ltd.com</text>

  <g class="lid-copy-block" transform="rotate(180 637 280)">
    <text class="brand-name brand-name-lid" x="637" y="200" text-anchor="middle">Brandell Group</text>
    <text class="brand-services" x="637" y="218" text-anchor="middle">WASHERS . STAMPINGS . ASSEMBLIES . BEARINGS</text>
    <text class="lid-url" x="637" y="258" text-anchor="middle">www.brandellgroup-ltd.com</text>
    <text class="lid-heading" x="637" y="278" text-anchor="middle">BRANDELL IS NOT JUST ANOTHER WASHER MANUFACTURER</text>
    <text class="lid-copy" x="637" y="291" text-anchor="middle">Brandell is recognized as a pioneer in the design of innovative stamping</text>
    <text class="lid-copy" x="637" y="302" text-anchor="middle">equipment. We have made our name through exceptional quality,</text>
    <text class="lid-copy" x="637" y="313" text-anchor="middle">our astute knowledge, and an enthusiastic desire to drive technology.</text>
  </g>

  <g class="recycle-mark">
    <circle class="recycle-ring" cx="655" cy="967" r="32" stroke-dasharray="50 17"/>
    <polygon class="recycle-head" points="676,935 694,947 672,955"/>
    <polygon class="recycle-head" points="654,1007 632,1004 646,988"/>
    <polygon class="recycle-head" points="618,950 628,930 640,948"/>
  </g>
  <g transform="rotate(180 582 967)">
    <text class="carton-number" x="582" y="972" text-anchor="middle">4</text>
    <text class="carton-label" x="582" y="982" text-anchor="middle">CARTON</text>
  </g>

  <g class="lid-copy-block" transform="rotate(180 637 1160)">
    <text class="brand-name brand-name-lid" x="637" y="1080" text-anchor="middle">Brandell Group</text>
    <text class="brand-services" x="637" y="1098" text-anchor="middle">WASHERS . STAMPINGS . ASSEMBLIES . BEARINGS</text>
    <text class="lid-url" x="637" y="1144" text-anchor="middle">www.brandellgroup-ltd.com</text>
    <text class="lid-heading" x="637" y="1165" text-anchor="middle">BRANDELL IS NOT JUST ANOTHER WASHER MANUFACTURER</text>
    <text class="lid-copy" x="637" y="1177" text-anchor="middle">Brandell is recognized as a pioneer in the design of innovative stamping</text>
    <text class="lid-copy" x="637" y="1189" text-anchor="middle">equipment. We have made our name through exceptional quality,</text>
    <text class="lid-copy" x="637" y="1201" text-anchor="middle">our astute knowledge, and an enthusiastic desire to drive technology.</text>
  </g>
</svg>
</body>
</html>
```